New Business Card Design*

We are a recruitment company based in Halbury/Cambridge England.
I have included our company logo which we want to remain the same.

What we are looking for is a new creative Business card which will really stand out!!

Contact Information for Business Card

Harriet Vance
email: Harriet@brelvix.co.uk
Address: Tolworth House
Ashgrove Innovation Park
Pelham Road
Halbury
KT9 3QD
Tel:01632 960418

```html
<!DOCTYPE html>
<html lang="en">
<head>
<meta charset="utf-8">
<title>Brelvix Business Card</title>
<link rel="stylesheet" href="https://fonts.googleapis.com/css2?family=Catamaran:wght@400;500;600&display=swap">
<style>
  :root {
    --page-bg: #e8e5e1;
    --card-white: #ffffff;
    --card-grey: #efefef;
    --brand-green: #8cc540;
    --brand-green-soft: #9bcf55;
    --brand-grey: #858388;
    --text-dark: #3c3c3e;
    --icon-dark: #434345;
    --hatch-grey: #e2e2e2;
    --band-dark: #2b2b2c;
  }
  * { margin: 0; padding: 0; box-sizing: border-box; }
  html, body {
    width: 1200px; height: 788px; overflow: hidden;
    background: var(--page-bg);
    font-family: "Catamaran", sans-serif;
  }
  .canvas { position: relative; width: 1200px; height: 788px; }
  .card {
    position: absolute; top: 260px;
    width: 480px; height: 268px; overflow: hidden;
    box-shadow: 0 2px 6px rgba(0,0,0,0.18);
  }
  .card--front { left: 110px; background: var(--card-white); }
  .card--back { left: 635px; background: var(--card-grey); }
  .accent-band {
    position: absolute; left: 0; top: 190px; width: 100%; height: 22px;
    background: var(--brand-green);
  }
  .card--back .accent-band { background: var(--brand-green-soft); }
  .base-panel { position: absolute; left: 0; top: 212px; width: 100%; height: 56px; }
  .card--front .base-panel { background: var(--hatch-grey); }
  .card--back .base-panel { background: linear-gradient(90deg, #2f2f30, var(--band-dark) 70%, #3a3a3b 82%, var(--band-dark)); }
  .wordmark {
    position: absolute; display: flex; align-items: center;
    color: var(--brand-grey); font-weight: 600; line-height: 1;
  }
  .wordmark__dot { border-radius: 50%; background: var(--brand-green); flex: none; }
  .card--front .wordmark { left: 0; width: 100%; justify-content: center; top: 66px; font-size: 54px; gap: 14px; }
  .card--front .wordmark__dot { width: 34px; height: 34px; }
  .card--back .wordmark { left: 235px; top: 70px; font-size: 40px; gap: 10px; }
  .card--back .wordmark__dot { width: 24px; height: 24px; }
  .contact { position: absolute; left: 27px; color: var(--text-dark); }
  .contact__row { position: absolute; left: 0; display: flex; align-items: flex-start; gap: 8px; white-space: nowrap; }
  .contact__icon { flex: none; }
  .contact__name { top: 27px; font-size: 17px; font-weight: 500; letter-spacing: 0.3px; text-transform: uppercase; align-items: center; }
  .contact__email { top: 75px; font-size: 12px; align-items: center; }
  .contact__phone { top: 111px; font-size: 12px; align-items: center; }
  .contact__address { top: 140px; font-size: 12px; line-height: 13px; }
  .contact__address .contact__icon { margin-top: 3px; }
</style>
</head>
<body>
<main class="canvas">
  <section class="card card--front" aria-label="Card front">
    <div class="wordmark"><span class="wordmark__dot"></span>Brelvix</div>
    <div class="accent-band"></div>
    <div class="base-panel" role="img" aria-label="Fine diagonal line pattern in light grey"></div>
  </section>

  <section class="card card--back" aria-label="Card back">
    <div class="contact">
      <div class="contact__row contact__name">
        <svg class="contact__icon" width="22" height="22" viewBox="0 0 22 22" aria-hidden="true">
          <circle cx="11" cy="11" r="11" fill="var(--icon-dark)"/>
          <circle cx="11" cy="8" r="3.6" fill="#fff"/>
          <path d="M4.5 17.5c1-3.6 3.5-5 6.5-5s5.5 1.4 6.5 5z" fill="#fff"/>
        </svg>
        Harriet Vance
      </div>
      <div class="contact__row contact__email">
        <svg class="contact__icon" width="15" height="15" viewBox="0 0 16 16" aria-hidden="true">
          <circle cx="8" cy="8" r="8" fill="var(--icon-dark)"/>
          <rect x="4.3" y="5.4" width="7.4" height="5.2" fill="#fff"/>
          <path d="M4.3 5.4 8 8.4l3.7-3" fill="none" stroke="var(--icon-dark)" stroke-width="0.9"/>
        </svg>
        Harriet@brelvix.co.uk
      </div>
      <div class="contact__row contact__phone">
        <svg class="contact__icon" width="15" height="15" viewBox="0 0 16 16" aria-hidden="true">
          <circle cx="8" cy="8" r="8" fill="var(--icon-dark)"/>
          <path d="M5.2 4.2l1.6-.3.9 2.1-1 .8c.5 1.1 1.3 1.9 2.4 2.4l.8-1 2.1.9-.3 1.6c-3.6.2-6.6-2.8-6.5-6.5z" fill="#fff"/>
        </svg>
        01632 960418
      </div>
      <div class="contact__row contact__address">
        <svg class="contact__icon" width="15" height="15" viewBox="0 0 16 16" aria-hidden="true">
          <circle cx="8" cy="8" r="8" fill="var(--icon-dark)"/>
          <path d="M8 4 4.2 7.4h1.1v4h2v-2.3h1.4v2.3h2v-4h1.1z" fill="#fff"/>
        </svg>
        <span>Tolworth House<br>Ashgrove Innovation Park<br>Pelham Road, Halbury, KT9 3QD</span>
      </div>
    </div>
    <div class="wordmark"><span class="wordmark__dot"></span>Brelvix</div>
    <div class="accent-band"></div>
    <div class="base-panel"></div>
  </section>
</main>
</body>
</html>
```